Meridale Counsel Corp Business Card design and layout

Meridale Counsel is a small, professional advisory firm specializing in business process consulting and advisory services. We are focused in the energy sector. The business card is to have a combination of blue shades and be professional and serious in nature. Investment banking, capital management, and professional service company card layouts should be used for similar templates

Target Market(s)

Medium to major corporations.

Industry/Entity Type

Consulting

Contact Information for Business Card

The card is to be professional looking in nature and must incorporate the company logo and name in some manner. A two sided design where the opposite side has a QR code and the logo is required.

Logo Text

Brastonhill Partners Inc.

Colors
0592cd
0455a3
3276b5
33a6d7
85cae6
85abd2
cee9f5
cedeed
ecf7fb

Requirements
Must have
• The card is to be professional and have space for employee, title, address, website, and phone numbers (office and cell). The layout must be some shades of blue.
Nice to have
• A space for embossing and/or some subtle gold highlights
Should not have
• Rainbow colours, unprofessional looking fonts (scribble, cursive writing)

```html
<!DOCTYPE html>
<html lang="en">
<head>
<meta charset="utf-8">
<title>Meridale Counsel Corp – Business Card</title>
<link rel="stylesheet" href="https://fonts.googleapis.com/css2?family=Cinzel:wght@700&family=Tinos:wght@400;700&display=swap">
<style>
  :root {
    --backdrop: #2e2f31;
    --card-white: #f7f8f9;
    --brand-blue: #0455a3;
    --brand-sky: #0592cd;
    --qr-tint: #cedeed;
    --back-deep: #24279a;
    --back-mid: #2f33ab;
    --back-light: #3d43b8;
    --ink-light: #ffffff;
    --rule: rgba(206, 222, 237, 0.55);
  }
  html, body {
    margin: 0;
    padding: 0;
    width: 1200px;
    height: 960px;
    overflow: hidden;
    background: var(--backdrop);
  }
  .canvas {
    width: 1200px;
    height: 960px;
    display: flex;
    flex-direction: column;
    align-items: center;
    justify-content: center;
    gap: 56px;
  }
  .card {
    width: 700px;
    height: 400px;
    box-sizing: border-box;
    border-radius: 4px;
    box-shadow: 0 10px 28px rgba(0, 0, 0, 0.45);
  }
  .card-front {
    position: relative;
    background: var(--card-white);
    display: flex;
    align-items: center;
    justify-content: center;
  }
  .front-wordmark {
    display: flex;
    align-items: center;
    gap: 16px;
  }
  .front-wordmark .mark-square {
    width: 24px;
    height: 24px;
    background: var(--brand-sky);
  }
  .front-wordmark .company-name {
    font-family: "Cinzel", serif;
    font-weight: 700;
    font-size: 42px;
    letter-spacing: 1px;
    color: var(--brand-blue);
    margin: 0;
  }
  .qr-area {
    position: absolute;
    right: 28px;
    bottom: 28px;
    width: 84px;
    height: 84px;
    background: var(--qr-tint);
    border: 2px solid var(--brand-blue);
    box-sizing: border-box;
  }
  .card-back {
    background: linear-gradient(135deg, var(--back-deep) 0%, var(--back-mid) 55%, var(--back-light) 100%);
    color: var(--ink-light);
    display: flex;
    flex-direction: column;
    align-items: center;
    padding-top: 50px;
    font-family: "Tinos", serif;
    text-align: center;
  }
  .back-wordmark {
    font-weight: 700;
    font-size: 30px;
    letter-spacing: 3px;
    text-transform: uppercase;
    margin: 0 0 22px;
  }
  .rule {
    width: 480px;
    height: 1px;
    background: var(--rule);
  }
  .employee-name {
    font-weight: 700;
    font-size: 25px;
    letter-spacing: 0.5px;
    text-transform: uppercase;
    margin: 10px 0 10px;
  }
  .employee-title {
    font-weight: 700;
    font-size: 18px;
    letter-spacing: 1px;
    text-transform: uppercase;
    margin: 8px 0 10px;
  }
  .contact-line,
  .contact-web {
    font-size: 18px;
    line-height: 24px;
    letter-spacing: 0.4px;
    margin: 0 0 4px;
  }
  .contact-web {
    letter-spacing: 1.5px;
    margin-bottom: 12px;
  }
</style>
</head>
<body>
  <main class="canvas">
    <section class="card card-front" aria-label="Card front">
      <div class="front-wordmark">
        <span class="mark-square"></span>
        <h1 class="company-name">Meridale Counsel Corp</h1>
      </div>
      <div class="qr-area" role="img" aria-label="QR code linking to the company website"></div>
    </section>

    <section class="card card-back" aria-label="Card back">
      <p class="back-wordmark">Meridale Counsel Corp</p>
      <div class="rule"></div>
      <p class="employee-name">Daniel Ashcombe, P.Eng</p>
      <div class="rule"></div>
      <p class="employee-title">President</p>
      <p class="contact-line">410, 718 - 6th Ave SW, Westbrook, AB, T4X 2M5</p>
      <p class="contact-line">O : 403-555-0174 &nbsp;&nbsp;C : 403-555-0192</p>
      <p class="contact-line">E : dashcombe@meridalecounsel.com</p>
      <p class="contact-web">www.meridalecounsel.com</p>
      <div class="rule"></div>
    </section>
  </main>
</body>
</html>
```